13 Tavo - new website design project

Our company Tavo Electrical is developing a new lead generation website focused on Electrical, LED Lighting and Solar Power. We need a high converting website.

Example of our current website is www.tavoelectrical.com.au You can take content from this website for this new design. Our colours are red, black and white. For our new website we would like to promote Tavo, Bright Days Ahead. Please listen to the jingle.

The below link is the company jingle that we have developed.
http://www.tunecraftaudio.com.au/tav-tc-v1/

The key for this brief is to generate leads for Electrical, LED Lighting (for commercial) and Solar Power & Storage.

Target Market(s)

Business owners in Melbourne Victoria

Number of Pages Required

4 page

Colors
ec1f27
ffffff

Requirements
Must have
• This page must be clean, be in line with company branding and a high converting lead website.

```html
<!DOCTYPE html>
<html lang="en">
<head>
<meta charset="utf-8">
<title>Tavo Electrical</title>
<link href="https://fonts.googleapis.com/css2?family=Source+Sans+3:wght@300;400;600;700&display=swap" rel="stylesheet">
<style>
:root{
  --red:#ec1f27;
  --black:#111111;
  --white:#ffffff;
  --dark-band:#2a2526;
  --grey-text:#6f6f6f;
  --footer-bg:#e9e9e9;
  --rule:#cfcfcf;
}
*{margin:0;padding:0;box-sizing:border-box}
html,body{width:1200px;height:4762px;overflow:hidden}
body{font-family:"Source Sans 3",sans-serif;background:var(--white);color:var(--black);position:relative}
.block{position:absolute;left:0;width:1200px}

/* header */
.site-header{top:0;height:135px;display:flex;align-items:center;justify-content:space-between;padding:0 30px 0 45px}
.brand{display:flex;align-items:center;gap:16px}
.brand-dot{width:64px;height:64px;border-radius:50%;background:var(--red)}
.brand-name{font-size:54px;font-weight:700;color:var(--black);line-height:1;letter-spacing:1px}
.brand-tag{font-size:20px;font-weight:400;color:var(--black);margin-top:4px}
.main-nav{display:flex;gap:44px;font-size:19px;letter-spacing:.5px}
.main-nav a{color:var(--black);text-decoration:none;padding-bottom:4px}
.main-nav a.current{border-bottom:2px solid var(--black)}

/* hero */
.hero{top:135px;height:480px;display:flex}
.hero-panel{flex:1;position:relative;display:flex;flex-direction:column;align-items:center;justify-content:center;gap:30px}
.hero-panel.electrical{background:linear-gradient(120deg,#c8322a,#1c6fb0 40%,#e5b531 70%,#2d2d2d)}
.hero-panel.solar{background:linear-gradient(180deg,#6e9ed3,#1d3f7a 55%,#26364f)}
.hero-panel.led{background:linear-gradient(135deg,#3a1a5c,#d43a8b 45%,#f2b640 75%,#ece7f0)}
.hero-title{font-size:36px;font-weight:700;color:var(--white);text-shadow:0 2px 6px rgba(0,0,0,.5)}
.hero-btn{border:2px solid var(--white);color:var(--white);font-size:16px;font-weight:700;padding:12px 0;width:245px;text-align:center;background:rgba(0,0,0,.15)}

/* intro */
.intro{top:615px;height:215px;background:var(--dark-band);color:#d8d4d4;font-size:17px;font-weight:300;line-height:1.55;text-align:center;padding:60px 60px 0}

/* why */
.why-photo{top:830px;height:710px;clip-path:polygon(0 0,100% 0,100% 100%,0 68%);background:radial-gradient(circle at 55% 30%,#e6eef5 0,#8a9cb0 25%,#3a4656 60%,#1c2530 100%)}
.section-title{position:absolute;left:0;width:1200px;text-align:center;font-size:32px;font-weight:700;color:var(--white);text-shadow:0 2px 6px rgba(0,0,0,.5)}

/* features */
.features{top:1580px}
.feature{position:absolute;width:300px;text-align:center}
.feature svg{display:block;margin:0 auto}
.feature h3{color:var(--red);font-size:27px;font-weight:700;line-height:1.2;margin-top:20px}
.feature p{color:var(--grey-text);font-size:15px;line-height:1.4;margin-top:22px;padding:0 10px}

/* customers */
.team-photo{top:2615px;height:730px;clip-path:polygon(0 0,100% 13%,100% 100%,0 100%);background:linear-gradient(135deg,#dfe4ea,#b7c0cb 45%,#5a4a44 75%,#2c2a2e)}
.client-row{top:3380px;display:flex;justify-content:center;gap:32px}
.client-tile{width:190px;height:112px;display:flex;align-items:center;justify-content:center;font-size:26px;font-weight:700;text-align:center;line-height:1.1;border:1px solid #e2e2e2}
.client-tile.velvetine{color:var(--red);background:var(--white)}
.client-tile.outback{color:var(--black);background:#f5e400}
.client-tile.heron{color:var(--white);background:var(--red)}
.client-tile.burger{color:#f5c400;background:#d71f1f}
.divider{top:3535px;left:175px;width:960px;border-top:1px solid var(--rule)}

/* testimonials */
.testimonial{position:absolute;left:150px;width:900px;display:flex;gap:30px}
.testimonial-thumb{width:230px;height:170px;flex:none;display:flex;flex-direction:column}
.thumb-name{height:40px;display:flex;align-items:center;justify-content:center;font-size:24px;font-weight:700}
.thumb-name.outback{background:#f5e400;color:var(--black)}
.thumb-name.velvetine{background:var(--white);color:var(--red)}
.thumb-photo{flex:1;background:linear-gradient(180deg,#c9c2b8,#7b6f66)}
.quote-head{color:var(--red);font-size:18px;font-weight:700;margin-top:12px}
.quote-body{color:var(--grey-text);font-size:15px;line-height:1.4;margin-top:12px}

/* footer */
.site-footer{top:4290px;height:472px;background:var(--footer-bg);display:flex;justify-content:space-between;padding:100px 90px 0 130px}
.footer-brand .brand-dot{width:120px;height:120px}
.footer-brand .brand-name{font-size:110px}
.footer-brand .brand-tag{font-size:36px}
.quick-links{text-align:right;padding-top:20px}
.quick-links h4{color:var(--red);font-size:19px;font-weight:700;margin-bottom:12px}
.quick-links a{display:block;color:var(--black);font-size:18px;text-decoration:none;line-height:1.75}
</style>
</head>
<body>

<header class="block site-header">
  <div class="brand">
    <div class="brand-dot"></div>
    <div>
      <div class="brand-name">TAVO</div>
      <div class="brand-tag">Bright Days Ahead</div>
    </div>
  </div>
  <nav class="main-nav">
    <a href="#">HOME</a>
    <a href="#" class="current">OUR STORY</a>
    <a href="#">OUR WORK</a>
    <a href="#">CONTACT</a>
  </nav>
</header>

<section class="block hero">
  <div class="hero-panel electrical" role="img" aria-label="Bundles of colourful electrical cables">
    <div class="hero-title">ELECTRICAL</div><div class="hero-btn">LEARN MORE</div>
  </div>
  <div class="hero-panel solar" role="img" aria-label="Solar panels under a blue sky">
    <div class="hero-title">SOLAR POWER</div><div class="hero-btn">LEARN MORE</div>
  </div>
  <div class="hero-panel led" role="img" aria-label="Close-up of coloured LED lights">
    <div class="hero-title">LED LIGHTING</div><div class="hero-btn">LEARN MORE</div>
  </div>
</section>

<section class="block intro">
  Tavo Electrical was formed to be an expert Electricity Contracting Company providing services to all Residential and Commercial Customers. With over 10 years of experience, Tavo Electrical has developed a highly-experienced team of professionals that ensure all our customer expectations are met.
</section>

<section class="block why-photo" role="img" aria-label="A lit energy-saving bulb standing among old incandescent bulbs">
  <h2 class="section-title" style="top:490px">WHY SHOULD YOU CHOOSE US</h2>
</section>

<section class="block features">
  <div class="feature" style="left:60px;top:0">
    <svg width="200" height="200" viewBox="0 0 200 200" fill="none" stroke="#ec1f27" stroke-width="2">
      <polygon points="60,95 69,118 94,118 74,133 81,157 60,143 39,157 46,133 26,118 51,118"/>
      <polygon points="100,45 111,73 141,73 117,91 126,120 100,102 74,120 83,91 59,73 89,73"/>
      <polygon points="140,95 149,118 174,118 154,133 161,157 140,143 119,157 126,133 106,118 131,118"/>
    </svg>
    <h3>Professional<br>Service</h3>
    <p>When you hire a Tavo Electrical Electrician you will get a professional and well presented Electrician that comes skilled and ready to do the job.</p>
  </div>
  <div class="feature" style="left:450px;top:0">
    <svg width="200" height="200" viewBox="0 0 200 200" fill="none" stroke="#ec1f27" stroke-width="2">
      <circle cx="100" cy="80" r="45"/><circle cx="100" cy="80" r="32"/>
      <polyline points="72,115 60,170 80,158 92,175 100,125"/>
      <polyline points="128,115 140,170 120,158 108,175 100,125"/>
    </svg>
    <h3>5 year workmanship<br>guarantee</h3>
    <p>You can buy with confidence as all our work has a 5 year workmanship guarantee. For your peace of mind, we unconditionally back our electrical work. We will come back to fix any problems at our own expense.</p>
  </div>
  <div class="feature" style="left:840px;top:0">
    <svg width="200" height="200" viewBox="0 0 200 200" fill="none" stroke="#ec1f27" stroke-width="2">
      <circle cx="100" cy="100" r="78"/>
      <path d="M124 72c-6-10-16-14-26-13-14 1-22 9-22 19 0 25 50 14 50 41 0 11-10 20-24 20-12 0-22-6-27-16" stroke-width="4"/>
      <line x1="100" y1="45" x2="100" y2="155" stroke-width="4"/>
    </svg>
    <h3>Value for<br>money</h3>
    <p>We provide extremely competitive pricing, which means you get value for money on quality that is comparable to the best in the industry.</p>
  </div>
  <div class="feature" style="left:270px;top:450px">
    <svg width="200" height="200" viewBox="0 0 200 200" fill="none" stroke="#ec1f27" stroke-width="2">
      <path d="M100 150c-30-20-30-60 0-95 30 35 30 75 0 95z"/>
      <path d="M92 150c-40 5-65-25-62-60 35 0 60 25 62 60z"/>
      <path d="M108 150c40 5 65-25 62-60-35 0-60 25-62 60z"/>
      <line x1="100" y1="150" x2="100" y2="175"/>
    </svg>
    <h3>Environmentally<br>friendly</h3>
    <p>We are committed to reducing carbon emissions by installing Solar Power and upgrading sites to LED Lighting. In addition to reducing the carbon emissions we recycle Fluorescent Tubes, Highbay Globes, Metal and Cardboard.</p>
  </div>
  <div class="feature" style="left:640px;top:450px">
    <svg width="200" height="200" viewBox="0 0 200 200" fill="none" stroke="#ec1f27" stroke-width="2">
      <path d="M100 25 165 45v55c0 40-30 65-65 80-35-15-65-40-65-80V45z"/>
    </svg>
    <h3>Fully<br>insured</h3>
    <p>Tavo Electrical is fully insured and equipped to handle breakdowns and service call outs.</p>
  </div>
</section>

<section class="block team-photo" role="img" aria-label="Business team meeting at a boardroom table with a bar chart on the wall">
  <h2 class="section-title" style="top:570px">OUR SATISFIED CUSTOMERS</h2>
</section>

<section class="block client-row">
  <div class="client-tile velvetine">Velvetine</div>
  <div class="client-tile outback">Outback Depot</div>
  <div class="client-tile heron">Heron Plumbing Supplies</div>
  <div class="client-tile burger">Burger Lane</div>
</section>

<div class="block divider"></div>

<section class="testimonials">
  <article class="testimonial" style="top:3575px">
    <div class="testimonial-thumb"><div class="thumb-name outback">Outback Depot</div><div class="thumb-photo" role="img" aria-label="Store interior with lit aisles"></div></div>
    <div><div class="quote-head">Executive, Outback Depot says</div>
    <p class="quote-body">“ The service, communication and after sales service of Tavo Electrical has been awesome. We would strongly recommend them to any business contemplating upgrading their lighting or any other electrical work. ”</p></div>
  </article>
  <article class="testimonial" style="top:3760px">
    <div class="testimonial-thumb"><div class="thumb-name velvetine">Velvetine</div><div class="thumb-photo" role="img" aria-label="Retail shop interior"></div></div>
    <div><div class="quote-head">M. Corliss, Eastfield VIC</div>
    <p class="quote-body">“ They clean up after the job, explained everything I needed to know and answered all questions, very professional. Will use them again in the future! ”</p></div>
  </article>
  <article class="testimonial" style="top:3945px">
    <div class="testimonial-thumb"><div class="thumb-name outback">Outback Depot</div><div class="thumb-photo" role="img" aria-label="Store interior with lit aisles"></div></div>
    <div><div class="quote-head">Executive, Outback Depot says</div>
    <p class="quote-body">“ The service, communication and after sales service of Tavo Electrical has been awesome. We would strongly recommend them to any business contemplating upgrading their lighting or any other electrical work. ”</p></div>
  </article>
  <article class="testimonial" style="top:4130px">
    <div class="testimonial-thumb"><div class="thumb-name velvetine">Velvetine</div><div class="thumb-photo" role="img" aria-label="Retail shop interior"></div></div>
    <div><div class="quote-head">M. Corliss, Eastfield VIC</div>
    <p class="quote-body">“ They clean up after the job, explained everything I needed to know and answered all questions, very professional. Will use them again in the future! ”</p></div>
  </article>
</section>

<footer class="block site-footer">
  <div class="brand footer-brand">
    <div class="brand-dot"></div>
    <div>
      <div class="brand-name">TAVO</div>
      <div class="brand-tag">Bright Days Ahead</div>
    </div>
  </div>
  <div class="quick-links">
    <h4>Quick Links</h4>
    <a href="#">Link 01</a><a href="#">Link 02</a><a href="#">Link 03</a><a href="#">Link 04</a>
  </div>
</footer>

</body>
</html>
```